Borlavex Management

We need a web design for a new consulting company, with clients all over the world. The company provides management consulting to the travel industry.

Logo files are attached.

Website must look very corporate and be responsive in design.

Management Consulting

```html
<!DOCTYPE html>
<html lang="en">
<head>
<meta charset="utf-8">
<title>Borlavex Management</title>
<link href="https://fonts.googleapis.com/css2?family=Cinzel:wght@400;600&family=Lato:ital,wght@0,400;0,700;1,400&family=Oswald:wght@500&display=swap" rel="stylesheet">
<style>
:root{
  --navy:#1c2357;
  --blue:#1e6fc0;
  --green:#4a9a1f;
  --green-dark:#3c7f17;
  --text:#444;
  --muted:#666;
  --light-band:#efefef;
  --footer:#333333;
  --footer-deep:#222222;
  --line:#dcdcdc;
}
*{box-sizing:border-box;margin:0;padding:0}
html,body{width:797px;height:1200px;overflow:hidden}
body{position:relative;background:#fff;font-family:'Lato',sans-serif;color:var(--text);font-size:11px}
.nowrap{white-space:nowrap}

/* header */
.site-header{position:absolute;left:0;top:0;width:797px;height:52px;background:linear-gradient(#fff,#f0f0f0);border-top:2px solid #5bb02b;border-bottom:1px solid #ccc}
.brand{position:absolute;left:88px;top:10px;display:flex;align-items:center;gap:6px}
.brand-dot{width:30px;height:30px;border-radius:50%;background:var(--blue);flex-shrink:0}
.brand-name{font-family:'Cinzel',serif;font-weight:600;font-size:21px;color:var(--navy);line-height:1}
.brand-name small{display:block;font-size:7.5px;color:var(--green);letter-spacing:1px;font-weight:400;margin-top:1px}
.main-nav{position:absolute;left:400px;top:0;display:flex;height:50px}
.main-nav a{width:78px;height:50px;border-left:1px solid #ddd;text-align:center;text-decoration:none;color:var(--navy);font-size:12px;padding-top:8px}
.main-nav a:last-child{border-right:1px solid #ddd}
.main-nav a.active{color:var(--blue);background:#f6f6f6}
.main-nav svg{display:block;margin:0 auto 5px}

/* hero */
.hero{position:absolute;left:0;top:52px;width:797px;height:296px;background:linear-gradient(90deg,#b7c8d0 0%,#9fb4be 35%,#3a4048 60%,#22262c 80%,#8ea3ad 100%)}
.hero-arrow{position:absolute;top:141px;width:26px;height:24px;background:#3a3f45;border:1px solid #777;display:flex;align-items:center;justify-content:center}
.hero-caption{position:absolute;left:88px;top:201px;padding:2px 6px 2px 7px;background:rgba(28,35,87,.75);border-left:3px solid var(--blue);font-family:'Oswald',sans-serif;font-size:15px;line-height:21px;color:#fff;text-transform:uppercase;white-space:nowrap}
.hero-dots{position:absolute;left:370px;top:276px;display:flex;gap:6px}
.hero-dots span{width:10px;height:10px;background:#fff;border:1px solid #ccc}
.hero-dots span.on{background:var(--green)}

/* welcome */
.welcome{position:absolute;left:0;top:348px;width:797px;height:164px;text-align:center}
.welcome-title{position:absolute;left:255px;top:20px;display:flex;align-items:center;gap:8px}
.welcome-title h1{font-family:'Cinzel',serif;font-weight:400;font-size:20px;color:var(--navy)}
.welcome-lead{position:absolute;left:0;width:797px;top:59px;font-style:italic;color:var(--navy);font-size:10px}
.welcome-copy{position:absolute;left:40px;width:717px;top:79px;font-size:9px;line-height:14px;color:#555;white-space:nowrap}
.btn{display:inline-block;background:linear-gradient(#5cb22b,var(--green-dark));color:#fff;text-decoration:none;font-weight:700;border-radius:2px}
.welcome .btn{position:absolute;left:368px;top:128px;width:63px;height:24px;line-height:24px;font-size:10px}

/* services */
.services{position:absolute;left:0;top:512px;width:797px;height:230px;background:var(--light-band)}
.service-card{position:absolute;top:36px;width:144px;height:175px;background:#fff;border:1px solid #ddd}
.service-icon{position:absolute;left:53px;top:-19px;width:36px;height:36px;border-radius:50%;background:var(--navy);border:3px solid #c9cbe0}
.service-photo{position:absolute;left:10px;top:10px;width:122px;height:82px;background:linear-gradient(135deg,#d8dde2,#8a98a8)}
.service-card h3{position:absolute;left:10px;top:97px;font-family:'Cinzel',serif;font-weight:600;font-size:14px;color:#222}
.service-card p{position:absolute;left:10px;top:118px;font-size:9px;line-height:13px;color:#555;white-space:nowrap}
.service-card .btn{position:absolute;left:10px;top:148px;width:45px;height:17px;line-height:17px;font-size:9px;text-align:center;font-weight:400}

/* info columns */
.info-col{position:absolute;top:762px}
.info-col h2{font-family:'Cinzel',serif;font-weight:600;font-size:14px;color:#222;padding-bottom:5px;border-bottom:1px solid var(--line);position:relative}
.info-col h2::after{content:"";position:absolute;left:0;bottom:-1px;width:46px;height:2px;background:var(--blue)}
.more-link{position:absolute;top:118px;left:0;font-size:9px;font-weight:700;color:var(--green);text-decoration:none}
.capabilities{left:88px;width:162px}
.capabilities ul{list-style:none;margin-top:8px}
.capabilities li{display:flex;align-items:center;gap:5px;font-size:9px;color:#444;height:16.5px;white-space:nowrap}
.capabilities li svg{flex-shrink:0}
.news{left:303px;width:128px}
.news dl{margin-top:8px;font-size:9px;line-height:12px;white-space:nowrap}
.news dt{color:var(--navy)}
.news dd{color:#555;margin-bottom:6px}
.experts{left:483px;width:228px}
.expert-row{display:flex;gap:5px;margin-top:12px}
.expert{width:72px;height:72px;position:relative;background:linear-gradient(#dde2e6,#b8c2cc);border:1px solid #ccc}
.expert span{position:absolute;left:0;bottom:0;width:100%;height:15px;background:var(--navy);color:#fff;font-size:9px;text-align:center;line-height:15px}
.divider{position:absolute;top:765px;width:1px;height:115px;background:#e5e5e5}

/* testimonials */
.testimonials{position:absolute;left:0;top:910px;width:797px;height:133px;background:#f4f4f4}
.testimonials h2{position:absolute;left:0;width:797px;top:16px;text-align:center;font-family:'Cinzel',serif;font-weight:400;font-size:15px;letter-spacing:1px;color:#222}
.testimonials h2::before,.testimonials h2::after{content:"";display:inline-block;width:82px;height:1px;background:#bbb;vertical-align:middle;margin:0 8px}
.client-avatar{position:absolute;left:90px;top:45px;width:58px;height:58px;border-radius:50%;border:2px solid var(--navy);background:linear-gradient(#f2e8d8,#d9c5a8)}
.quote{position:absolute;left:172px;top:47px;width:535px;font-style:italic;font-size:8.4px;line-height:14px;color:#555;border-bottom:1px solid #ddd;padding-bottom:4px;white-space:nowrap}
.client-name{position:absolute;left:172px;top:100px;font-size:9.5px;font-weight:700;color:#333}

/* footer */
.site-footer{position:absolute;left:0;top:1043px;width:797px;height:132px;background:var(--footer);border-top:2px solid var(--blue);color:#ddd}
.foot-col{position:absolute;top:12px}
.foot-col h4{font-weight:400;font-size:13px;color:#fff;padding-bottom:4px;border-bottom:1px solid #555;margin-bottom:7px}
.quick ul{list-style:none}
.quick li{font-size:9px;height:16.5px;display:flex;gap:7px}
.contact p{display:flex;gap:8px;font-size:9px;line-height:11px;margin-bottom:9px}
.contact svg{flex-shrink:0;margin-top:1px}
.newsletter p{font-size:8.5px;line-height:12px;margin-bottom:6px}
.email-field{width:138px;height:18px;background:#fff;color:#999;font-size:7.5px;padding:4px 5px}
.newsletter .btn{margin-top:8px;width:70px;height:19px;line-height:19px;font-size:10px;text-align:center}
.social{display:flex;gap:7px}
.social span{width:20px;height:20px;border-radius:50%;background:#6a6a6a}
.foot-brand{margin-top:10px;display:flex;align-items:center;gap:4px}
.foot-brand i{width:20px;height:20px;border-radius:50%;background:#ddd;display:block}
.foot-brand b{font-family:'Cinzel',serif;font-weight:600;font-size:14px;color:#eee;line-height:1}
.foot-brand b small{display:block;font-size:6px;font-weight:400;letter-spacing:.5px}
.copyright{position:absolute;left:0;top:1175px;width:797px;height:25px;background:var(--footer-deep);color:#ddd;font-size:9px;text-align:center;line-height:25px}
</style>
</head>
<body>

<header class="site-header">
  <div class="brand"><span class="brand-dot"></span><div class="brand-name">BORLAVEX<small>MANAGEMENT</small></div></div>
  <nav class="main-nav">
    <a href="#" class="active"><svg width="18" height="16" viewBox="0 0 18 16"><path d="M1 8 9 1l8 7h-2v7h-4v-5H7v5H3V8z" fill="#1e6fc0"/></svg>Home</a>
    <a href="#"><svg width="20" height="16" viewBox="0 0 20 16"><circle cx="7" cy="4" r="3.5" fill="#1c2357"/><circle cx="14" cy="4" r="3.5" fill="#1c2357"/><path d="M1 15c0-5 12-5 12 0zM9 15c0-5 10-5 10 0z" fill="#1c2357"/></svg>About Us</a>
    <a href="#"><svg width="18" height="16" viewBox="0 0 18 16"><circle cx="7" cy="7" r="5" fill="none" stroke="#1c2357" stroke-width="3" stroke-dasharray="2 1.5"/><circle cx="14" cy="12" r="3" fill="none" stroke="#1c2357" stroke-width="2"/></svg>Services</a>
    <a href="#"><svg width="16" height="16" viewBox="0 0 16 16"><rect x="2" y="1" width="11" height="14" fill="none" stroke="#1c2357" stroke-width="1.6"/><path d="M5 5h5M5 8h5M5 11h3" stroke="#1c2357" stroke-width="1.4"/></svg>Contact</a>
  </nav>
</header>

<section class="hero" role="img" aria-label="Businessman in a suit sketching an airplane outline on a glass screen">
  <div class="hero-arrow" style="left:5px"><svg width="8" height="10"><path d="M7 1 2 5l5 4" stroke="#fff" stroke-width="2" fill="none"/></svg></div>
  <div class="hero-arrow" style="left:765px"><svg width="8" height="10"><path d="M1 1l5 4-5 4" stroke="#fff" stroke-width="2" fill="none"/></svg></div>
  <div class="hero-caption">We provides management<br>consulting to the travel industry.</div>
  <div class="hero-dots"><span></span><span class="on"></span><span></span><span></span></div>
</section>

<section class="welcome">
  <div class="welcome-title"><span class="brand-dot"></span><h1>Welcome to Borlavex</h1></div>
  <p class="welcome-lead">Lorem ipsum dolor sit amet, consectetur adipiscing eli Vestibulum efficitur pellentesque mi, ut vestibulum mauris sagittis at.</p>
  <p class="welcome-copy">Aliquam vitae magna aliquet, molestie est eget, ultricies arcu. Nunc non luctus turpis, et sollicitudin sem. In at vehicula tellus. Nulla vel eleifend nulla, quis ultrices<br>metus. Nunc finibus nisi ac congue tempor. Nulla elementum, leo non vehicula lacinia, velit libero hendrerit purus, sed feugiat felis orci id erat. Cras ultrices vehicula<br>lectus a porttitor. Nunc eu enim at sem varius aliquet Vestibulum eu dolor erat. Aenean luctus venenatis</p>
  <a href="#" class="btn">Read More</a>
</section>

<section class="services">
  <article class="service-card" style="left:87px"><span class="service-icon"></span><div class="service-photo" role="img" aria-label="Team meeting around a laptop"></div><h3>Consulting</h3><p>Lorem ipsum dolor consectetur<br>adipiscing elit estibueff</p><a href="#" class="btn">MORE</a></article>
  <article class="service-card" style="left:247px"><span class="service-icon"></span><div class="service-photo" role="img" aria-label="Colleagues reviewing documents"></div><h3>Analysis</h3><p>Lorem ipsum dolor consectetur<br>adipiscing elit estibueff</p><a href="#" class="btn">MORE</a></article>
  <article class="service-card" style="left:407px"><span class="service-icon"></span><div class="service-photo" role="img" aria-label="Hands pointing at charts on a tablet"></div><h3>Services</h3><p>Lorem ipsum dolor consectetur<br>adipiscing elit estibueff</p><a href="#" class="btn">MORE</a></article>
  <article class="service-card" style="left:567px"><span class="service-icon"></span><div class="service-photo" role="img" aria-label="Business team discussing strategy at a laptop"></div><h3>Strategy</h3><p>Lorem ipsum dolor consectetur<br>adipiscing elit estibueff</p><a href="#" class="btn">MORE</a></article>
</section>

<section class="info-col capabilities">
  <h2>Our Capabilities</h2>
  <ul>
    <li><svg width="11" height="11"><circle cx="5.5" cy="5.5" r="5.5" fill="#1c2357"/><path d="M3 5.5l2 2 3.5-4" stroke="#fff" stroke-width="1.4" fill="none"/></svg>At vero eos et accusamus et iusto</li>
    <li><svg width="11" height="11"><circle cx="5.5" cy="5.5" r="5.5" fill="#1c2357"/><path d="M3 5.5l2 2 3.5-4" stroke="#fff" stroke-width="1.4" fill="none"/></svg>Dignissimos ducimus qui blanditiis</li>
    <li><svg width="11" height="11"><circle cx="5.5" cy="5.5" r="5.5" fill="#1c2357"/><path d="M3 5.5l2 2 3.5-4" stroke="#fff" stroke-width="1.4" fill="none"/></svg>Daesentium voluptatum deleniti atque</li>
    <li><svg width="11" height="11"><circle cx="5.5" cy="5.5" r="5.5" fill="#1c2357"/><path d="M3 5.5l2 2 3.5-4" stroke="#fff" stroke-width="1.4" fill="none"/></svg>Corrupti quos dolores et quas</li>
    <li><svg width="11" height="11"><circle cx="5.5" cy="5.5" r="5.5" fill="#1c2357"/><path d="M3 5.5l2 2 3.5-4" stroke="#fff" stroke-width="1.4" fill="none"/></svg>Alestias excepturi sint occaecati cup</li>
  </ul>
  <a href="#" class="more-link">View More →</a>
</section>
<div class="divider" style="left:275px"></div>
<section class="info-col news">
  <h2>What's New?</h2>
  <dl>
    <dt>March 14, 2013</dt><dd>Lorem ipsum dolor sit amet,<br>consectetur adipiscing elit. Sed...</dd>
    <dt>February 20, 2013</dt><dd>Lorem ipsum dolor sit amet,<br>consectetur adipiscing elit. Sed...</dd>
  </dl>
  <a href="#" class="more-link">Archive →</a>
</section>
<div class="divider" style="left:458px"></div>
<section class="info-col experts">
  <h2>Our Leading Experts</h2>
  <div class="expert-row">
    <div class="expert" role="img" aria-label="Portrait of expert Nora Vellin"><span>Nora Vellin</span></div>
    <div class="expert" role="img" aria-label="Portrait of expert Ada Sorrel"><span>Ada Sorrel</span></div>
    <div class="expert" role="img" aria-label="Portrait of expert Owen Trask"><span>Owen Trask</span></div>
  </div>
  <a href="#" class="more-link">Explore →</a>
</section>

<section class="testimonials">
  <h2>Client Testimonials</h2>
  <div class="client-avatar" role="img" aria-label="Portrait of the client"></div>
  <p class="quote">“ Lorem ipsdolor sit amet, consectetur adipiscing elit. Donec sit amet nulla vitae tortor iaculis commodo. Nulla interdum dui vitae lectus malesuada<br>ac dignissim mi vehicula. Nullam ornare vulputate sem vitae convallis. Proin et faucibus eros. Nam id rutrum risus, quis eleifend tortor. Nulla scelerisque<br>vitae ante vitae, rhoncus pellentesque turpis. Donec feugiat malesuada justo, quis porta urna egestas nec. Duis nec lobortis justo, ac varius ante. ”</p>
  <p class="client-name">Mr. Calder Brisk</p>
</section>

<footer class="site-footer">
  <div class="foot-col quick" style="left:87px;width:80px">
    <h4>Quick Links</h4>
    <ul><li>›<span>Home</span></li><li>›<span>About Us</span></li><li>›<span>Services</span></li><li>›<span>Contact Us</span></li></ul>
  </div>
  <div class="foot-col contact" style="left:205px;width:155px">
    <h4>Contact Information</h4>
    <p><svg width="8" height="11" viewBox="0 0 8 11"><path d="M4 0a4 4 0 0 1 4 4c0 3-4 7-4 7S0 7 0 4a4 4 0 0 1 4-4z" fill="#ddd"/><circle cx="4" cy="4" r="1.5" fill="#333"/></svg><span>Lorem ipsum dolor consectetuer adipiscing elit, sed diam nonummy bitasa street:395001</span></p>
    <p><svg width="10" height="10" viewBox="0 0 10 10"><path d="M2 0h2l1 3-1.5 1a6 6 0 0 0 2.5 2.5L7 5l3 1v2c0 1-1 2-2 2C4 10 0 6 0 2 0 1 1 0 2 0z" fill="#ddd"/></svg><span>+12 555010200</span></p>
    <p><svg width="10" height="8" viewBox="0 0 10 8"><rect width="10" height="8" fill="#ddd"/><path d="M0 0l5 4 5-4" stroke="#333" fill="none"/></svg><span>info@borlavex-mail.com</span></p>
  </div>
  <div class="foot-col newsletter" style="left:414px;width:138px">
    <h4>Newsletter Sign Up</h4>
    <p>Lorem ipsudolr sit coec adipiscing elitsite amet</p>
    <div class="email-field">Email Address</div>
    <a href="#" class="btn">SUBSCRIBE</a>
  </div>
  <div class="foot-col" style="left:606px;width:104px">
    <h4>Follow Us</h4>
    <div class="social"><span></span><span></span><span></span><span></span></div>
    <div class="foot-brand"><i></i><b>BORLAVEX<small>MANAGEMENT</small></b></div>
  </div>
</footer>
<div class="copyright">Copyright © 2014 - Borlavex.com</div>

</body>
</html>
```